Business card design needed

We are 2 artists starting up a studio by the water in Sydney ...where we can work and display our art...would like the back ground to be Navy and white stripe...nautical...and the name The Clay Nook to be bold and the main wording...not nautical...if possible thought the A for art could be an easel ...ie the capital A using the cross bar as the platform that paint would be circles of colour....would like the main wording in Black but the easel A in colour
Hope u are able to help
thanku Lorna Vesk
as I will be away in a week for 4 weeks could u please send all info to Jodie Minchens email....she can contact me and we can go ahead asap....

Industry/Entity Type

Artists

Contact Information for Business Card

THE CLAY NOOK

Halloways Dock House
The Bend..41 Kelvane Rd..Mosman 2088 Sydney

Jodi Minchen..0417583091..jodiminchen@mailwave.example
Lorn Vesk...0413862714..lvesk@quillnet.example.au

```html
<!DOCTYPE html>
<html lang="en">
<head>
<meta charset="utf-8">
<title>The Clay Nook – Business Card</title>
<link rel="stylesheet" href="https://fonts.googleapis.com/css2?family=PT+Sans:wght@400;700&display=swap">
<style>
  :root {
    --navy: #1f3d99;
    --white: #ffffff;
    --red: #ec1c24;
    --ink: #111111;
    --text-grey: #3a3a3a;
    --backdrop: #eeeeee;
  }
  html, body {
    margin: 0;
    padding: 0;
    width: 1200px;
    height: 778px;
    overflow: hidden;
    background: var(--backdrop);
  }
  .card {
    position: absolute;
    left: 50px;
    top: 69px;
    width: 1100px;
    height: 640px;
    background: var(--white);
    overflow: hidden;
    font-family: "PT Sans", sans-serif;
    box-shadow: 0 2px 8px rgba(0,0,0,0.12);
  }
  .stripe-band {
    position: absolute;
    left: 0;
    top: 420px;
    width: 1100px;
    height: 220px;
    background: repeating-linear-gradient(
      to bottom,
      var(--navy) 0 4px,
      var(--white) 4px 9px
    );
  }
  .card-shapes {
    position: absolute;
    inset: 0;
  }
  .brand-name {
    position: absolute;
    left: 191px;
    top: 150px;
    margin: 0;
    font-weight: 700;
    color: var(--ink);
    font-size: 82px;
    line-height: 1;
    letter-spacing: -0.5px;
  }
  .brand-name .article {
    font-size: 46px;
    margin-right: 10px;
  }
  .contacts {
    position: absolute;
    left: 168px;
    top: 316px;
    margin: 0;
    padding: 0;
    list-style: none;
    color: var(--text-grey);
  }
  .contact {
    font-size: 23px;
    line-height: 44px;
    white-space: nowrap;
  }
  .contact .person {
    font-size: 29px;
    text-transform: uppercase;
  }
  .address {
    position: absolute;
    left: 630px;
    top: 492px;
    width: 420px;
    margin: 0;
    font-style: normal;
    text-align: center;
    color: var(--white);
    font-size: 23px;
    line-height: 34px;
    white-space: nowrap;
  }
</style>
</head>
<body>
  <main class="card">
    <div class="stripe-band"></div>

    <svg class="card-shapes" width="1100" height="640" viewBox="0 0 1100 640">
      <path class="navy-field" fill="var(--navy)"
        d="M0,0 H1100 V395 C1020,370 980,300 900,270 C820,210 700,190 600,150 C480,110 350,120 250,110 C150,100 60,130 0,190 Z"/>
      <path class="white-field" fill="var(--white)"
        d="M30,410 H650 C670,470 640,540 580,580 C480,625 220,615 120,592 C60,572 40,500 60,460 C45,440 35,425 30,410 Z"/>
      <path class="paint-splash" role="img" aria-label="Red paint splash" fill="var(--red)"
        d="M560,470 C610,425 760,432 860,418 C960,404 1050,408 1100,398 V640 H630 C590,600 540,540 560,470 Z"/>
    </svg>

    <h1 class="brand-name"><span class="article">the</span>Clay Nook</h1>

    <ul class="contacts">
      <li class="contact"><span class="person">Minchen</span> : 0417583091 | jodiminchen@mailwave.example</li>
      <li class="contact"><span class="person">Lorn Vesk</span> : 0413862714 | lvesk@quillnet.example.au</li>
    </ul>

    <address class="address">
      Halloways Dock House, The Bend..41<br>
      Kelvane Rd. Mosman 2088,<br>
      Sydney Lorn
    </address>
  </main>
</body>
</html>
```